依頼詳細
【背景】
弊社は平成17年の創業以来、パチンコ店の広告物を主に企画提案〜制作、折込などの代理店業を行ってきました。
しかし、パチンコ業界の規制強化などの理由から、パチンコ業界以外の業種の広告物やBtoBの販促企画•制作、また最近では農家のブランディングなどの仕事にシフトしてきています。
そのような状況の中、弊社の代表自らもMBAのビジネススクールに通いマーケティング等を学び直しており、今後は現状の制作メインの仕事だけではなく、さらに川上のマーケティングや広告戦略といった、もっとクライアントに入り込んだお手伝いが出来る力をつけていきたいと考えています。
その為には再度、組織の再構築、強みを活かせる組織づくりを行っていく必要があり、設立10年を前に第二創業といった心づもりで企業理念を変更しようと考えています。
また、企業理念はこの会社は何の為に存在しているのかを言語化したものであり、在職中のスタッフだけではなく、今後採用予定の方にも共感した上で働いていただきたいと考えています。

【仕様】
・A3縦で制作してください
・納品はイラレデータでお願いします
・イメージは実際の経営理念から想像してください
記載項目
企業理念

Creative Happy!
-社会のHappy!
-顧客のHappy!
-仲間のHappy!
-家族のHappy!
-自分のHappy!

会社ロゴ

【解説(ココは記載不要です)】
Creative Happy! … 広告物を作るのではなく、その先にあるHappyを作っているという意識。
例えば、ケーキ屋さんのDMを作る際、「ケーキ屋さんのDMをつくっている」という意識ではなく「家族で美味しそうにこのケーキを食べている姿」つまり「その先のHappy!」を意識・想像して作ることが出来れば、仕事の質に大きな差が生じると考えています。

-社会のHappy!
-顧客のHappy!
-仲間のHappy!
-家族のHappy!
-自分のHappy!
仕事をする上で「Happy!を考える順番」を意味しています。
希望イメージ
シンプル 複雑
単色 カラフル
暗い 明るい
日常 高級
遊び心 厳粛
未来的 伝統的
女性的 男性的
希望する色
納品ファイル
• イラストレーター形式 (.ai)
補足説明
■ 選んだ理由

まずイメージが明るくHAPPYな感じがしたこと
次に非常にわかりやすいビジュアルでストーリーを作ってくださったことが
kitazono-teさんのデザインを選んだ理由です。

■ 提案者全員のお礼・コメント

皆様にはご提案をいただき感謝いたします。
今回、大変多くの方からご提案をいただき、素敵なデザインが他にもあり社内でも選考するのに随分意見が出ました。

今回は弊社の社内的なポスターでしたが、弊社は広告代理業を行っているためチラシやDMなど他のグラフィックデザインも仕事として発生しています。(携帯電話のチラシなど)
またお願いすることもあるかと思いますので、どうぞよろしくお願いします。

```html
<!DOCTYPE html>
<html lang="ja">
<head>
<meta charset="utf-8">
<title>Creative Happy! 企業理念ポスター</title>
<link rel="stylesheet" href="https://fonts.googleapis.com/css2?family=Archivo+Black&family=Noto+Sans+JP:wght@900&display=swap">
<style>
  :root {
    --paper: #ffffff;
    --frame: #d9d9d9;
    --navy: #1b3a8a;
    --red: #c3141c;
    --white: #ffffff;
    --ink: #111111;
  }
  * { margin: 0; padding: 0; box-sizing: border-box; }
  html, body { width: 853px; height: 1200px; overflow: hidden; background: var(--paper); }
  .poster {
    position: relative;
    width: 853px; height: 1200px;
    background: var(--paper);
    border: 6px solid var(--frame);
  }
  .headline {
    position: absolute;
    left: 44px; top: 180px;
    width: 380px;
    color: var(--navy);
    font-family: "Archivo Black", sans-serif;
    line-height: 1;
    text-align: center;
  }
  .headline .line-creative { display: block; font-size: 62px; letter-spacing: -1px; }
  .headline .line-happy { display: block; font-size: 96px; letter-spacing: -3px; margin-top: 2px; }
  .company {
    position: absolute;
    left: 560px; top: 300px;
    width: 250px;
    display: flex; align-items: center; gap: 10px;
    color: var(--ink);
    font-family: "Archivo Black", sans-serif;
    font-size: 22px;
    line-height: 1.1;
  }
  .company .mark { width: 26px; height: 26px; background: var(--ink); flex: none; }
  .values {
    position: absolute;
    left: 28px; top: 528px;
    width: 782px; height: 640px;
    background: var(--red);
    padding: 20px 14px;
    display: flex; flex-direction: column; justify-content: space-between;
    list-style: none;
  }
  .value-row { display: flex; align-items: center; gap: 6px; height: 112px; }
  .cell {
    width: 80px; height: 104px;
    display: flex; align-items: center; justify-content: center;
    color: var(--white);
  }
  .cell.kanji { font-family: "Noto Sans JP", sans-serif; font-weight: 900; font-size: 62px; }
  .cell.latin { font-family: "Archivo Black", sans-serif; font-size: 92px; padding-bottom: 10px; }
  .cell.boxed {
    background: var(--navy);
    border: 4px solid var(--white);
  }
  .cell.latin.boxed { font-size: 80px; }
</style>
</head>
<body>
<main class="poster">
  <h1 class="headline">
    <span class="line-creative">Creative</span>
    <span class="line-happy">Happy!</span>
  </h1>

  <div class="company">
    <span class="mark" aria-hidden="true"></span>
    <span class="name">SORAMI Planning Studio</span>
  </div>

  <ol class="values">
    <li class="value-row">
      <span class="cell kanji boxed">社</span><span class="cell kanji boxed">会</span><span class="cell kanji">の</span>
      <span class="cell latin boxed">H</span><span class="cell latin">a</span><span class="cell latin">p</span><span class="cell latin">p</span><span class="cell latin">y</span><span class="cell latin">!</span>
    </li>
    <li class="value-row">
      <span class="cell kanji boxed">顧</span><span class="cell kanji boxed">客</span><span class="cell kanji">の</span>
      <span class="cell latin">H</span><span class="cell latin boxed">a</span><span class="cell latin">p</span><span class="cell latin">p</span><span class="cell latin">y</span><span class="cell latin">!</span>
    </li>
    <li class="value-row">
      <span class="cell kanji boxed">仲</span><span class="cell kanji boxed">間</span><span class="cell kanji">の</span>
      <span class="cell latin">H</span><span class="cell latin">a</span><span class="cell latin boxed">p</span><span class="cell latin">p</span><span class="cell latin">y</span><span class="cell latin">!</span>
    </li>
    <li class="value-row">
      <span class="cell kanji boxed">家</span><span class="cell kanji boxed">族</span><span class="cell kanji">の</span>
      <span class="cell latin">H</span><span class="cell latin">a</span><span class="cell latin">p</span><span class="cell latin boxed">p</span><span class="cell latin">y</span><span class="cell latin">!</span>
    </li>
    <li class="value-row">
      <span class="cell kanji boxed">自</span><span class="cell kanji boxed">分</span><span class="cell kanji">の</span>
      <span class="cell latin">H</span><span class="cell latin">a</span><span class="cell latin">p</span><span class="cell latin">p</span><span class="cell latin boxed">y</span><span class="cell latin">!</span>
    </li>
  </ol>
</main>
</body>
</html>
```